Varnok Power Systems ( LED lIghting Service Company) flyer

A single sheet folded in half, like a book, highlighting LED lighting retrofits. Use stock pictures for different bulbs. We sell and install all fixtures. We install 48" tubes, corn bulbs, UFO lights, high bay lights, gas station canopy lights, parking lot lights,
Should include:
Reduce electric bill by as much as 70%
Improved quality of light
Zero maintenance cost
Eliminates eye strain and headache pain
Produces no heat
5 year warranty
Work with power companies to achieve greatest rebate.
Complete turnkey solution provider
Target Market(s)
Business owners, facility managers, VP of operations
Industry/Entity Type
It Company
Colors
Designer to choose colors to be used in the design.
Requirements
Must have
- High quality photos,
Nice to have
- Fonts, colors and designs are up to the designers

```html
<!DOCTYPE html>
<html lang="en">
<head>
<meta charset="utf-8">
<title>Varnok Power Systems – LED Lighting Flyer</title>
<link rel="stylesheet" href="https://fonts.googleapis.com/css2?family=Ubuntu:wght@300;400;500;700&family=Open+Sans:wght@400;700&display=swap">
<style>
  :root {
    --ink: #15161f;
    --red: #e3202a;
    --white: #ffffff;
    --muted: #d9dae0;
    --page: #ececec;
  }
  * { box-sizing: border-box; margin: 0; padding: 0; }
  html, body { width: 900px; height: 1200px; overflow: hidden; background: var(--page); }
  body { position: relative; font-family: "Ubuntu", sans-serif; color: var(--white); }

  .spread { position: absolute; left: 67px; width: 766px; background: var(--ink); overflow: hidden; }
  .spread--outer { top: 52px; height: 540px; }
  .spread--inner { top: 605px; height: 542px; }
  .spread svg.art { position: absolute; inset: 0; }

  .intro-copy { position: absolute; left: 31px; top: 14px; width: 118px; font-size: 7.2px; line-height: 10.6px; color: var(--muted); font-weight: 300; }
  .intro-copy p + p { margin-top: 10px; }

  .store-info { position: absolute; left: 28px; top: 424px; width: 170px; font-size: 10px; line-height: 13px; }
  .store-info strong { font-weight: 700; display: block; }
  .store-info .web { margin-top: 10px; display: block; }
  .store-info .phone { margin-top: 10px; display: block; color: var(--red); }

  .brand-box { position: absolute; left: 413px; top: 0; width: 121px; height: 98px; background: var(--red);
    display: flex; align-items: center; justify-content: center; text-align: center; }
  .brand-name { font-family: "Ubuntu", sans-serif; font-weight: 500; color: var(--white); font-size: 13px; line-height: 15px; }
  .brand-mark { position: absolute; left: 232px; top: 446px; width: 140px; text-align: center; }
  .brand-mark .brand-name { font-size: 17px; line-height: 20px; }

  .cover-title { position: absolute; left: 420px; top: 462px; font-size: 19px; line-height: 24px; font-weight: 300; }

  .fixture-list-block { position: absolute; left: 432px; top: 48px; width: 170px; }
  .fixture-lead { font-family: "Open Sans", sans-serif; font-weight: 700; color: var(--red); font-size: 11.5px; line-height: 14px; margin-bottom: 6px; }
  .fixture-list { list-style: none; font-size: 11.5px; line-height: 19.5px; }

  .benefits-box { position: absolute; left: 609px; top: 0; width: 131px; height: 203px; background: var(--red); padding: 53px 6px 0 10px; }
  .benefits-list { list-style: none; font-size: 8.2px; line-height: 10.6px; font-weight: 300; }

  .side-copy { position: absolute; left: 432px; top: 228px; width: 310px; font-size: 8.2px; line-height: 11.5px; color: var(--muted); font-weight: 300; }

  .about-lead { position: absolute; left: 43px; top: 212px; width: 300px; font-size: 8.6px; line-height: 12.2px; color: var(--red); }
  .about-col { position: absolute; top: 304px; width: 142px; font-size: 6.8px; line-height: 9.6px; color: var(--muted); font-weight: 300; }
  .about-col--a { left: 43px; }
  .about-col--b { left: 205px; }

  .product-dots { position: absolute; left: 30px; top: 455px; display: flex; gap: 19px; }
  .product-dot { width: 63px; height: 63px; border-radius: 50%; background: var(--white);
    border: 3px solid var(--red); border-left-color: var(--white); border-top-color: var(--white); position: relative; }
  .product-dot span { position: absolute; inset: 8px; border-radius: 50%; background: radial-gradient(circle at 50% 45%, #ffffff 0, #e6e6e4 30%, #a9abb0 62%, #6e7076 100%); }
</style>
</head>
<body>

<section class="spread spread--outer">
  <svg class="art" width="766" height="540" viewBox="0 0 766 540">
    <defs>
      <radialGradient id="storeTone" cx="0.62" cy="0.45" r="0.75">
        <stop offset="0" stop-color="#fbf8f3"/>
        <stop offset="0.35" stop-color="#ece6dc"/>
        <stop offset="0.7" stop-color="#c9c0b3"/>
        <stop offset="1" stop-color="#8d8378"/>
      </radialGradient>
      <radialGradient id="bulbTone" cx="0.5" cy="0.45" r="0.55">
        <stop offset="0" stop-color="#f4f2ea"/>
        <stop offset="0.55" stop-color="#c9c5b6"/>
        <stop offset="1" stop-color="#15161f" stop-opacity="0"/>
      </radialGradient>
    </defs>
    <path d="M250 0 Q160 210 186 540" fill="none" stroke="var(--red)" stroke-width="9"/>
    <path role="img" aria-label="Photo: shopper comparing LED bulbs on bright store shelves" d="M272 0 L766 0 L766 355 Q500 440 192 350 Q180 150 272 0 Z" fill="url(#storeTone)"/>
    <path d="M192 350 Q500 440 766 355 L766 372 Q500 452 192 362 Z" fill="var(--red)"/>
    <ellipse role="img" aria-label="Photo: assorted LED bulbs and corn lamps" cx="653" cy="440" rx="105" ry="62" fill="url(#bulbTone)"/>
  </svg>

  <div class="intro-copy">
    <p>It is a long established fact that a reader will be distracted by the readable content of a page when looking at its layout. The point of using Lorem Ipsum is that it has a more-or-less normal distribution of letters, as opposed to using 'Content here, content here', making it look like readable English. Many desktop publishing packages and web page editors now use Lorem Ipsum as their default model text, and a search for 'lorem ipsum' will uncover many web sites still in their infancy. Various versions have evolved over the years, sometimes by accident, sometimes on purpose (injected humour and the like).</p>
    <p>There are many variations of passages of Lorem Ipsum available, but the majority have suffered alteration in some form, by injected humour, or randomised words which don't look even slightly believable.</p>
  </div>

  <div class="brand-box"><span class="brand-name">Varnok Power<br>Systems</span></div>

  <div class="store-info">
    <strong>Varnok Power Systems</strong>
    Lighting store in the<br>Millbrook, GA, USA
    <span class="web">varnokpower.com</span>
    <span class="phone">Call us: 555.214.3870</span>
  </div>

  <div class="brand-mark"><span class="brand-name">Varnok Power<br>Systems</span></div>

  <h1 class="cover-title">LED lights<br>Retrofitting</h1>
</section>

<section class="spread spread--inner">
  <svg class="art" width="766" height="542" viewBox="0 0 766 542">
    <defs>
      <radialGradient id="hallTone" cx="0.5" cy="0.62" r="0.7">
        <stop offset="0" stop-color="#f2fbff"/>
        <stop offset="0.25" stop-color="#bfe0ee"/>
        <stop offset="0.6" stop-color="#6fa6c0"/>
        <stop offset="1" stop-color="#3d6f88"/>
      </radialGradient>
      <radialGradient id="ceilingTone" cx="0.62" cy="0.35" r="0.75">
        <stop offset="0" stop-color="#fbfbf9"/>
        <stop offset="0.35" stop-color="#dcdbd6"/>
        <stop offset="0.75" stop-color="#a9a7a1"/>
        <stop offset="1" stop-color="#6f6d69"/>
      </radialGradient>
    </defs>
    <path role="img" aria-label="Photo: long corridor lit by LED ceiling panels" d="M0 0 L383 0 L383 132 Q200 210 0 150 Z" fill="url(#hallTone)"/>
    <path d="M0 150 Q200 210 383 132 L383 142 Q200 222 0 160 Z" fill="var(--red)"/>
    <path d="M383 322 Q570 290 766 318 L766 330 Q570 302 383 334 Z" fill="var(--red)"/>
    <path role="img" aria-label="Photo: office ceiling with recessed LED panels" d="M383 334 Q570 302 766 330 L766 542 L383 542 Z" fill="url(#ceilingTone)"/>
  </svg>

  <div class="fixture-list-block">
    <p class="fixture-lead">We sell and install<br>all fixtures</p>
    <ul class="fixture-list">
      <li>48” tubes,</li>
      <li>Corn bulbs,</li>
      <li>UFO lights,</li>
      <li>High bay lights,</li>
      <li>Gas station canopy lights,</li>
      <li>Parking lot lights</li>
    </ul>
  </div>

  <div class="benefits-box">
    <ul class="benefits-list">
      <li>Reduce electric bill by as much as 70%</li>
      <li>Improved quality of light</li>
      <li>Zero maintenance cost</li>
      <li>Eliminates eye strain and headache pain</li>
      <li>Produces no heat</li>
      <li>5 year warranty</li>
      <li>Work with power companies to achieve greatest rebate.</li>
      <li>Complete turnkey solution provider</li>
    </ul>
  </div>

  <p class="side-copy">Lorem Ipsum is simply dummy text of the printing and typesetting industry. Lorem Ipsum has been the industry's standard dummy text ever since the 1500s, when an unknown printer took a galley of type and scrambled it to make a type specimen book. It has survived not only five centuries</p>

  <p class="about-lead">Varnok Power Systems is the southeast's most trusted LED lighting retrofitters. We take pride in our service and remain flexible with all of our clients to ensure no disruption to their business. Our team works around your schedule to make the switch as smooth as possible. We have partnered with the top manufactures of LED lighting to provide you with the highest quality product on the market.</p>

  <p class="about-col about-col--a">We convert all of the old fixtures whether it is fluorescent as in office ceilings to large warehouse lights to the appropriate LED solution. On most projects we lower the monthly electric bill by up to 70%. Over past year we have reduced our customers in Excess of $1 million U.S dollars in electric costs. The lighting installed is the highest quality available and we work with all of the Major Utility companies in the southeast to get customers large rebates for doing this to their buildings.</p>
  <p class="about-col about-col--b">We convert all of the old fixtures whether it is fluorescent as in office ceilings to large warehouse lights to the appropriate LED solution. On most projects we lower the monthly electric bill by up to 70%. Over past year we have reduced our customers in Excess of $1 million U.S dollars in electric costs. The lighting installed is the highest quality available and we work with all of the Major Utility companies in the southeast to get customers large rebates for doing this to their buildings.</p>

  <div class="product-dots">
    <div class="product-dot" role="img" aria-label="Photo: LED downlight"><span></span></div>
    <div class="product-dot" role="img" aria-label="Photo: LED spotlight fitting"><span></span></div>
    <div class="product-dot" role="img" aria-label="Photo: slim LED panel"><span></span></div>
    <div class="product-dot" role="img" aria-label="Photo: recessed LED light"><span></span></div>
  </div>
</section>

</body>
</html>
```